Ridgeway Insulcoat Works Spray Foam Appications website

We need a custom website for our company, www.ridgewayinsulcoatworks.example. We need something we can modify by adding/changing content, photos, updated projects, etc. We are a commercial contractor specializing in Spray Foam applications. We want the website to be very creative and easy to navigate. The main points of the website are to showcase our projects, and describe our scope of services. We provide spray foam applications to the residential and commercial market. We offer Spray Foam roofing applications, as well as Spray Foam interior insulation applications. We also provide Roof Restoration Coating Systems to refurbish old and failing metal roofs. We would be ok with a one page web design if we can get the scope of our services to flow in a single page. The designer can decide if single or multiple pages works best for our business. One of the suppliers we work with is www.vantrexo.example.

Target Market(s)

Residential Home Builders, General Contractors, Commercial Construction Companies, Property Management Groups.

Industry/Entity Type

Insulation

Number of Pages Required

5+ page

Font styles to use
Serif
Sans Serif

Colors

Designer to choose colors to be used in the design.

Requirements
Must have
• We already have a Wix page, so website must be a Wix theme design. Nice easy to navigate format. Color matched to our current logo theme. We already have brochures and would like for it to match what's already in the hands of some of our customers. Need to be able to manage content to update photos, projects, scope of service, etc., via Wix. Current hold/splash page is hosted at www.ridgewayinsulcoatworks.example. We would also like to have this video posted on the home page: https://www.videohost.example/watch?v=QzT4kLp9wXe&feature=share
Nice to have
• I have attached some splash videos, being able to incorporate these somehow without being overpowering would be nice.

```html
<!DOCTYPE html>
<html lang="en">
<head>
<meta charset="utf-8">
<title>Ridgeway Insulcoat Works — Spray Foam Applications</title>
<link href="https://fonts.googleapis.com/css2?family=Roboto:ital,wght@0,300;0,400;0,500;0,700;0,900;1,400;1,700;1,900&family=Roboto+Mono:wght@500;700&display=swap" rel="stylesheet">
<style>
:root{
  --yellow:#f5b21b;
  --dark:#2f2f2f;
  --darker:#262626;
  --ink:#222;
  --light:#f3f3f3;
  --white:#fff;
}
*{margin:0;padding:0;box-sizing:border-box}
html,body{width:1200px;height:3746px;overflow:hidden}
body{font-family:'Roboto',Arial,sans-serif;color:var(--ink);background:var(--white);position:relative}
.section{position:absolute;left:0;width:1200px}
.abs{position:absolute}
.btn{position:absolute;background:var(--yellow);color:var(--white);font-size:10px;font-weight:700;text-transform:uppercase;display:flex;align-items:center;justify-content:center;letter-spacing:.3px;box-shadow:0 3px 8px rgba(0,0,0,.12)}
.section-title{position:absolute;left:161px;font-size:22px;font-weight:700;text-transform:uppercase;color:var(--ink)}
.section-title span{color:var(--yellow)}
.lead{position:absolute;left:161px;font-size:9.5px;line-height:23px;color:#444;width:640px}

/* header / hero */
.hero{top:0;height:524px;background:linear-gradient(180deg,#4a4a48 0%,#3b3b3a 45%,#2e2e2d 100%)}
.brand{position:absolute;display:flex;align-items:center;gap:8px}
.brand-mark{width:40px;height:40px;border-radius:50%;border:3px solid var(--yellow)}
.brand-name{font-size:12.5px;font-weight:700;color:var(--yellow);text-transform:uppercase;letter-spacing:.4px;line-height:1.2;width:120px}
.nav{position:absolute;left:391px;top:38px;display:flex;gap:29px;font-size:11.5px;font-weight:500;color:var(--white);text-transform:uppercase}
.nav .active{color:var(--yellow)}
.header-rule{position:absolute;left:0;top:90px;width:1200px;height:1px;background:rgba(255,255,255,.16)}
.hero-band{position:absolute;left:0;top:177px;width:1178px;height:99px;background:rgba(80,80,78,.85)}
.hero-title{position:absolute;right:163px;top:196px;text-align:right;font-size:29px;font-weight:700;line-height:31px;color:var(--white)}
.hero-title em{display:block;color:var(--yellow);font-weight:900;font-style:italic}
.hero-text{position:absolute;right:161px;top:286px;width:600px;text-align:right;font-size:10.5px;font-weight:700;font-style:italic;line-height:22.5px;color:var(--white)}
.dots{position:absolute;left:577px;top:494px;display:flex;gap:10px;align-items:center}
.dots i{display:block;width:7px;height:7px;border-radius:50%;background:var(--white)}
.dots i.on{width:14px;height:14px;background:var(--yellow);border:2px solid #fff}

/* about */
.about{top:524px;height:453px}
.eyebrow{position:absolute;font-size:12px;font-weight:500;color:var(--ink)}
.eyebrow::after{content:"";display:block;width:54px;height:2px;background:var(--yellow);margin-top:9px}
.ghost-years{position:absolute;left:0;top:100px;font-size:40px;font-weight:900;letter-spacing:4px;color:#f2f2f2;font-family:'Roboto Mono',monospace}
.texture-area{position:absolute;left:0;top:135px;width:400px;height:180px;background:#fbfbfb}
.about-intro{position:absolute;left:161px;top:102px;font-family:'Roboto Mono',monospace;font-weight:700;font-size:13.5px;letter-spacing:-.3px;line-height:22.5px;color:var(--ink);white-space:nowrap}
.checks{position:absolute;left:161px;top:217px;list-style:none}
.checks li{display:flex;align-items:center;gap:10px;height:24px;font-size:9.5px;color:#b5b5b5}
.checks li::before{content:"";width:9px;height:9px;border-radius:50%;border:3px solid #fff;box-shadow:0 0 0 1.5px var(--yellow);background:var(--yellow)}
.play{position:absolute;border-radius:50%;border:2px solid var(--yellow);display:flex;align-items:center;justify-content:center;background:var(--white)}
.watch-link{position:absolute;font-size:9.5px;color:#aaa;text-decoration:underline}
.cards{position:absolute;left:611px;top:61px;width:427px;height:333px}
.card{position:absolute;width:214px;height:167px;background:var(--white);box-shadow:0 2px 10px rgba(0,0,0,.08);text-align:center;padding-top:28px}
.card h3{font-size:13px;font-weight:500;color:var(--ink);text-transform:uppercase;margin-top:8px;margin-bottom:10px}
.card p{font-size:8.5px;line-height:18px;color:#aaa;padding:0 28px}
.hub{position:absolute;left:184px;top:136px;width:60px;height:60px;border-radius:50%;background:var(--dark);border:3px solid var(--white)}

/* services */
.services{top:977px;height:485px;background:var(--light)}
.service{position:absolute;top:191px;width:278px}
.photo{display:block;width:100%}
.service h4{font-size:12.5px;font-weight:500;margin-top:14px}
.more{display:flex;align-items:center;gap:8px;font-size:9.5px;color:var(--yellow);margin-top:10px}

/* video band */
.video-band{top:1462px;height:339px;background:linear-gradient(90deg,#2e2e2e,#3a3a3a 60%,#333)}
.video-band h2{position:absolute;left:160px;width:430px;top:64px;text-align:center;font-size:13px;font-weight:700;color:var(--white);text-transform:uppercase}
.video-band p{position:absolute;left:160px;width:430px;top:103px;text-align:center;font-size:9.5px;line-height:22.5px;color:#9a9a9a}

/* work */
.work{top:1801px;height:647px}
.work-row{position:absolute;left:161px;width:877px;height:187px;background:var(--white);box-shadow:0 2px 14px rgba(0,0,0,.07)}
.work-row h4{position:absolute;font-size:12.5px;font-weight:500}
.work-row p{position:absolute;width:385px;font-size:8.5px;line-height:16.5px;color:#9a9a9a}
.work-row .more{position:absolute;margin:0}

/* hire band */
.hire{top:2448px;height:176px;background:linear-gradient(90deg,#2b2b2b,#3b3b3b 50%,#303030)}
.hire small{position:absolute;left:191px;top:59px;font-size:7px;letter-spacing:1.5px;color:#888;text-transform:uppercase}
.hire h2{position:absolute;left:191px;top:78px;font-size:15px;font-weight:700;line-height:26px;color:var(--white);text-transform:uppercase}
.hire h2 span{display:block;color:var(--yellow)}

/* testimonial */
.testimonial{top:2624px;height:530px}
.avatar{position:absolute;left:161px;top:153px;width:75px;height:75px;border-radius:50%;border:3px solid var(--yellow);background:linear-gradient(#d6d6d6,#9d9d9d)}
.person{position:absolute;left:161px;top:239px;font-size:11px;font-weight:700;font-style:italic;color:var(--yellow)}
.quote{position:absolute;left:191px;top:273px;width:360px;font-size:9.5px;font-style:italic;line-height:22.5px;color:#444}
.qmark{position:absolute;font-size:34px;font-weight:900;color:#ddd;font-family:Georgia,serif}
.arrows{position:absolute;left:352px;top:381px;display:flex;gap:6px}
.promo-text{position:absolute;left:698px;color:var(--white)}

/* stats */
.stats{top:3154px;height:140px}
.stat{position:absolute;top:17px;display:flex;align-items:center;gap:18px}
.stat b{display:block;font-size:29px;font-weight:500;color:var(--ink)}
.stat span{font-size:11px;font-weight:500;color:#333}

/* partners */
.partners{top:3294px;height:150px;background:var(--light)}
.badge{position:absolute;top:44px;width:128px;height:60px;border:1px solid #dcdcdc;display:flex;align-items:center;justify-content:center}
.badge i{display:block;width:46px;height:12px;background:#d9d9d9}

/* footer */
.footer{top:3444px;height:256px;background:var(--dark);color:var(--white)}
.footer h5{position:absolute;top:58px;font-size:14px;font-weight:700;text-transform:uppercase}
.footer .about-text{position:absolute;left:161px;top:111px;width:210px;font-size:9.5px;line-height:15px;color:#ddd}
.follow{position:absolute;left:161px;top:199px;display:flex;align-items:center;gap:10px;font-size:9.5px;color:var(--yellow)}
.follow i{display:block;width:7px;height:7px;border-radius:50%;background:var(--white)}
.links{position:absolute;left:385px;top:109px;display:grid;grid-template-columns:77px 88px 50px;row-gap:10px;font-size:9.5px;color:#ddd;text-transform:uppercase}
.links .active{color:var(--yellow);text-decoration:underline}
.news{position:absolute;left:614px;width:200px;font-size:9.5px;line-height:15px;color:#ddd}
.contact{position:absolute;left:838px;top:113px;width:210px;font-size:9.5px;line-height:15px;color:#ddd}
.contact .label{color:var(--yellow)}
.contact div{margin-bottom:5px}
.copyright{top:3700px;height:46px;background:var(--darker);display:flex;align-items:center;justify-content:center;font-size:9px;color:var(--white)}
.copyright em{color:var(--yellow)}
</style>
</head>
<body>

<!-- HERO -->
<header class="section hero">
  <div class="abs" role="img" aria-label="Crew of workers walking on a foam-coated roof" style="left:0;top:0;width:1200px;height:524px;background:linear-gradient(180deg,rgba(110,110,105,.35),rgba(40,40,40,.1) 60%,rgba(0,0,0,.15))"></div>
  <div class="brand" style="left:161px;top:24px">
    <span class="brand-mark"></span>
    <span class="brand-name">Ridgeway Insulcoat Works</span>
  </div>
  <nav class="nav">
    <span class="active">Home</span><span>About Us</span><span>Services</span><span>Work</span><span>Blog</span><span>Contact Us</span>
  </nav>
  <a class="btn" style="left:900px;top:22px;width:137px;height:45px">Request a Quote</a>
  <div class="header-rule"></div>
  <div class="hero-band"></div>
  <h1 class="hero-title">We Are The Undisputed Leaders<em>IN THIS INDUSTRY!</em></h1>
  <p class="hero-text">Lorem ipsum dolor amet 3 wolf moon unicorn selfies bitters keffiyeh c squid edison bulb synth roof party palo santo you probably haven't heard of them lo-fi. Raw denim cardigan before they could if and andy sold out four loko kombucha, YOLO lumbersexual squid poke kogi photo booth synth</p>
  <a class="btn" style="left:929px;top:378px;width:109px;height:37px">Learn More</a>
  <div class="dots"><i></i><i class="on"></i><i></i></div>
</header>

<!-- ABOUT -->
<section class="section about">
  <div class="texture-area" role="img" aria-label="Faint decorative texture behind the about text"></div>
  <div class="ghost-years">20YEAR</div>
  <div class="eyebrow" style="left:161px;top:60px">About Us</div>
  <p class="about-intro">Lorem ipsum dolor amet 3 wolf moon unicorn selfies<br>bitters keffiyeh cornhole squid edison bulb synth roof<br>party palo santo you probably haven't heard of them lo-fi.<br>Raw denim cardigan before they sold out</p>
  <ul class="checks">
    <li>Lorem ipsum dolor is amet ningun postekam</li>
    <li>Lorem ipsum dolor is amet ningun postekam</li>
    <li>Lorem ipsum dolor is amet ningun postekam</li>
    <li>Lorem ipsum dolor is amet ningun postekam</li>
    <li>Lorem ipsum dolor is amet ningun postekam</li>
  </ul>
  <a class="btn" style="left:161px;top:357px;width:108px;height:35px">Learn More</a>
  <div class="play" style="left:285px;top:355px;width:38px;height:38px">
    <svg width="12" height="14" viewBox="0 0 12 14"><path d="M1 1l10 6-10 6z" fill="var(--yellow)"/></svg>
  </div>
  <span class="watch-link" style="left:331px;top:368px">Watch Video</span>

  <div class="cards">
    <div class="card" style="left:0;top:0">
      <svg width="28" height="16" viewBox="0 0 28 16"><path d="M4 1h20l3 14H1z M8 1l-2 14 M14 1v14 M20 1l2 14 M2.5 8h23" fill="none" stroke="var(--yellow)" stroke-width="1.3"/></svg>
      <h3>Roof Services</h3><p>Lorem ipsum dolor amet 3 wolf moon unicorn selfies bitters keffiyeh cornhole squid edison bulb synth roof</p>
    </div>
    <div class="card" style="left:213px;top:0">
      <svg width="28" height="16" viewBox="0 0 28 16"><path d="M4 1h20l3 14H1z M8 1l-2 14 M14 1v14 M20 1l2 14 M2.5 8h23" fill="none" stroke="var(--yellow)" stroke-width="1.3"/></svg>
      <h3>Foam Services</h3><p>Lorem ipsum dolor amet 3 wolf moon unicorn selfies bitters keffiyeh cornhole squid edison bulb synth roof</p>
    </div>
    <div class="card" style="left:0;top:167px">
      <svg width="28" height="16" viewBox="0 0 28 16"><path d="M4 1h20l3 14H1z M8 1l-2 14 M14 1v14 M20 1l2 14 M2.5 8h23" fill="none" stroke="var(--yellow)" stroke-width="1.3"/></svg>
      <h3>Experts</h3><p>Lorem ipsum dolor amet 3 wolf moon unicorn selfies bitters keffiyeh cornhole squid edison bulb synth roof</p>
    </div>
    <div class="card" style="left:213px;top:167px">
      <svg width="28" height="16" viewBox="0 0 28 16"><path d="M4 1h20l3 14H1z M8 1l-2 14 M14 1v14 M20 1l2 14 M2.5 8h23" fill="none" stroke="var(--yellow)" stroke-width="1.3"/></svg>
      <h3>Quality &amp; Skills</h3><p>Lorem ipsum dolor amet 3 wolf moon unicorn selfies bitters keffiyeh cornhole squid edison bulb synth roof</p>
    </div>
    <div class="hub"></div>
  </div>
</section>

<!-- SERVICES -->
<section class="section services">
  <h2 class="section-title" style="top:57px">Get To Know Our <span>Best Services</span></h2>
  <p class="lead" style="top:104px">Lorem ipsum dolor amet vaporware snackwave intelligentsia meh, selvage shoreditch semiotics. Kombucha bicycle rights selvage, hoodie wolf marfa kogi man braid pok pok craft beer PBR&amp;B fashion axe quinoa. Drinking vinegar literally banh mi, salvia roof partyifst</p>
  <a class="btn" style="left:929px;top:85px;width:109px;height:36px">View All</a>

  <div class="service" style="left:161px">
    <div class="photo" role="img" aria-label="Hangar with freshly foamed roof under blue sky" style="height:186px;background:linear-gradient(180deg,#3d6aa8 0%,#8fb0d6 40%,#b9a77d 60%,#d8c690 100%)"></div>
    <h4>Lorem Ipsum Dolor Amet</h4>
    <div class="more">Discover More <svg width="16" height="6" viewBox="0 0 16 6"><path d="M0 3h14M11 0.5l3 2.5-3 2.5" fill="none" stroke="var(--yellow)"/></svg></div>
  </div>
  <div class="service" style="left:461px">
    <div class="photo" role="img" aria-label="Warehouse interior with spray foam insulated walls and hoses on floor" style="height:186px;background:linear-gradient(180deg,#b7b2a9 0%,#e5e2dc 45%,#cfcac2 75%,#8a877f 100%)"></div>
    <h4>Lorem Ipsum Dolor Amet</h4>
    <div class="more">Discover More <svg width="16" height="6" viewBox="0 0 16 6"><path d="M0 3h14M11 0.5l3 2.5-3 2.5" fill="none" stroke="var(--yellow)"/></svg></div>
  </div>
  <div class="service" style="left:761px">
    <div class="photo" role="img" aria-label="Long coated metal roof stretching to the horizon" style="height:186px;background:linear-gradient(180deg,#4a76b8 0%,#93b3da 45%,#b9c1cc 60%,#7f8894 100%)"></div>
    <h4>Lorem Ipsum Dolor Amet</h4>
    <div class="more">Discover More <svg width="16" height="6" viewBox="0 0 16 6"><path d="M0 3h14M11 0.5l3 2.5-3 2.5" fill="none" stroke="var(--yellow)"/></svg></div>
  </div>
</section>

<!-- VIDEO BAND -->
<section class="section video-band">
  <h2>Lorem Ipsum Dolor Amet Ningun Postekam</h2>
  <p>Lorem ipsum dolor amet vaporware literally put a bird on it photo booth, humblebrag occupy four loko leggings offal church-key farm-to-table pabst. Banjo mlkshk ugh intelligentsia enamel pin. Edison bulb gastropub craft beer hella disrupt offal sriracha listicle tote bag ennui swag tbh umami schlitz. Etsy hashtag pok pok kombucha, echo park palo santo trust fund whatever listicle man bun copper mug activated charcoal cornhole</p>
  <a class="btn" style="left:323px;top:235px;width:109px;height:38px">Watch More</a>
  <div class="abs" role="img" aria-label="Video preview of a coated roof at a plant with trees behind" style="left:612px;top:58px;width:426px;height:221px;background:linear-gradient(180deg,#5c6c84 0%,#8c98aa 25%,#3c4a3a 32%,#6e6e6c 45%,#8f8f8b 100%)"></div>
  <div class="play" style="left:777px;top:151px;width:36px;height:36px;border:none">
    <svg width="12" height="14" viewBox="0 0 12 14"><path d="M1 1l10 6-10 6z" fill="var(--yellow)"/></svg>
  </div>
  <span class="watch-link" style="left:822px;top:163px;color:#fff">Watch Video</span>
</section>

<!-- WORK -->
<section class="section work">
  <h2 class="section-title" style="top:56px">Some Of The <span>Recent Work</span> Done</h2>
  <p class="lead" style="top:103px">Lorem ipsum dolor amet vaporware snackwave intelligentsia meh, selvage shoreditch semiotics. Kombucha bicycle rights selvage, hoodie wolf marfa kogi man braid pok pok craft beer PBR&amp;B fashion axe quinoa. Drinking vinegar literally banh mi, salvia roof partyifst</p>

  <div class="work-row" style="top:189px">
    <svg class="abs" style="left:0;top:0" width="427" height="187" viewBox="0 0 427 187" role="img" aria-label="Roof project photo with yellow tint">
      <path d="M0 0H427L395 93 427 187H0z" fill="#e9b830"/>
      <circle cx="213" cy="93" r="17" fill="none" stroke="#fff" stroke-width="1.5"/>
      <circle cx="211" cy="91" r="6" fill="none" stroke="#fff" stroke-width="1.5"/>
      <path d="M215 95l5 5" stroke="#fff" stroke-width="1.5"/>
    </svg>
    <h4 style="left:457px;top:28px">Lorem Ipsum Dolor Amet</h4>
    <p style="left:457px;top:54px">Lorem ipsum dolor amet vaporware snackwave intelligentsia meh, selvage shoreditch semiotics. Kombucha bicycle rights selvage, hoodie wolf marfa kogi man braid pok pok craft beer PBR&amp;B fashion axe quinoa. Drinking vinegar literally banh mi, salvia roof party slow-carb typewriter thundercats pour-over yr fam four loko humblebrag art party lorem ipsum dolor amet ningun .postedam if any lorem</p>
    <div class="more" style="left:457px;top:149px">View More <svg width="16" height="6" viewBox="0 0 16 6"><path d="M0 3h14M11 0.5l3 2.5-3 2.5" fill="none" stroke="var(--yellow)"/></svg></div>
  </div>

  <div class="work-row" style="top:400px">
    <h4 style="left:31px;top:28px">Lorem Ipsum Dolor Amet</h4>
    <p style="left:31px;top:54px">Lorem ipsum dolor amet vaporware snackwave intelligentsia meh, selvage shoreditch semiotics. Kombucha bicycle rights selvage, hoodie wolf marfa kogi man braid pok pok craft beer PBR&amp;B fashion axe quinoa. Drinking vinegar literally banh mi, salvia roof party slow-carb typewriter thundercats pour-over yr fam four loko humblebrag art party lorem ipsum dolor amet ningun .postedam if any lorem</p>
    <div class="more" style="left:31px;top:149px">View More <svg width="16" height="6" viewBox="0 0 16 6"><path d="M0 3h14M11 0.5l3 2.5-3 2.5" fill="none" stroke="var(--yellow)"/></svg></div>
    <svg class="abs" style="left:451px;top:0" width="426" height="187" viewBox="0 0 426 187" role="img" aria-label="Large industrial building with coated roof">
      <defs><linearGradient id="bldg" x1="0" y1="0" x2="0" y2="1"><stop offset="0" stop-color="#4d7dc0"/><stop offset=".45" stop-color="#a9c1dd"/><stop offset=".55" stop-color="#b5a98a"/><stop offset="1" stop-color="#d9c99b"/></linearGradient></defs>
      <path d="M0 0H426V187H0L33 93z" fill="url(#bldg)"/>
    </svg>
  </div>
</section>

<!-- HIRE -->
<section class="section hire">
  <small>Looking for quality?</small>
  <h2>Time To Hire Us<span>For Your Upcoming Project</span></h2>
  <a class="btn" style="left:929px;top:70px;width:109px;height:36px">Hire Us</a>
</section>

<!-- TESTIMONIAL + PROMO -->
<section class="section testimonial">
  <div class="avatar" role="img" aria-label="Customer portrait"></div>
  <div class="person">Dario Vennell - Costumer</div>
  <span class="qmark" style="left:158px;top:262px">&ldquo;</span>
  <p class="quote">Lorem ipsum dolor amet vaporware snackwave intelligentsia meh, selvage shoreditch semiotics. Kombucha bicycle rights selvage, hoodie wolf marfa kogi man braid pok pok craft beer PBR&amp;B fashion axe quinoa. Drinking vinegar literally banh mi, salvia roof party slow-carb typewriter thundercats pour-over yr fam four</p>
  <span class="qmark" style="left:563px;top:337px">&rdquo;</span>
  <div class="arrows">
    <svg width="18" height="8" viewBox="0 0 18 8"><path d="M18 4H2M5 1L1 4l4 3" fill="none" stroke="#999"/></svg>
    <svg width="18" height="8" viewBox="0 0 18 8"><path d="M0 4h16M13 1l4 3-4 3" fill="none" stroke="var(--yellow)"/></svg>
  </div>

  <svg class="abs" style="left:612px;top:60px" width="426" height="429" viewBox="0 0 426 429"><path d="M0 0H426V429H72z" fill="var(--dark)"/></svg>
  <div class="promo-text" style="top:158px;font-size:9.5px;font-weight:500">LET'S GET BIGGER</div>
  <div class="promo-text" style="top:180px;font-size:15px;font-weight:700">TOGETHER</div>
  <p class="promo-text" style="left:704px;top:211px;width:200px;font-size:9.5px;font-style:italic;line-height:18px;color:#ddd">Lorem ipsum dolor amet vaporware literally put a bird on it photo booth, humblebrag occupy four loko leggings offal church-key of lorem ips farm-to-table pabst. Banjo mlkshk ugh anyboi</p>
  <a class="btn" style="left:704px;top:298px;width:109px;height:37px">See More</a>
  <div class="abs" role="img" aria-label="Worker in protective suit spraying foam insulation into a wall frame" style="left:938px;top:249px;width:175px;height:240px;background:linear-gradient(90deg,#a87c4d 0%,#d9cfc2 35%,#eeeeee 65%,#c9c9c9 100%)"></div>
</section>

<!-- STATS -->
<section class="section stats">
  <div class="stat" style="left:161px">
    <svg width="52" height="64" viewBox="0 0 52 64"><circle cx="26" cy="15" r="13" fill="#8c8c8c"/><path d="M2 64V44c0-8 7-14 15-14h18c8 0 15 6 15 14v20z" fill="#8c8c8c"/><path d="M26 32l-4 8 4 20 4-20z" fill="#fff"/></svg>
    <div><b>515</b><span>Happy Clients</span></div>
  </div>
  <div class="stat" style="left:516px">
    <svg width="64" height="64" viewBox="0 0 64 64"><g fill="#8c8c8c"><circle cx="32" cy="32" r="22"/><rect x="27" y="2" width="10" height="12"/><rect x="27" y="50" width="10" height="12"/><rect x="2" y="27" width="12" height="10"/><rect x="50" y="27" width="12" height="10"/><rect x="27" y="2" width="10" height="12" transform="rotate(45 32 32)"/><rect x="27" y="50" width="10" height="12" transform="rotate(45 32 32)"/><rect x="2" y="27" width="12" height="10" transform="rotate(45 32 32)"/><rect x="50" y="27" width="12" height="10" transform="rotate(45 32 32)"/></g><circle cx="32" cy="32" r="11" fill="#fff"/><circle cx="32" cy="32" r="6" fill="#8c8c8c"/></svg>
    <div><b>400+</b><span>Projects Done</span></div>
  </div>
  <div class="stat" style="left:870px">
    <svg width="66" height="64" viewBox="0 0 66 64"><g fill="#8c8c8c"><path d="M8 54L40 20l6 6-32 34z"/><circle cx="48" cy="16" r="13"/><path d="M10 6l8 2 34 38 6 2 6 8-8 8-8-6-2-6L8 14 6 6z"/></g><circle cx="50" cy="13" r="5" fill="#fff"/></svg>
    <div><b>200</b><span>Working Hours</span></div>
  </div>
</section>

<!-- PARTNERS -->
<section class="section partners">
  <div class="badge" style="left:161px"><i></i></div>
  <div class="badge" style="left:311px"><i></i></div>
  <div class="badge" style="left:461px"><i></i></div>
  <div class="badge" style="left:612px"><i></i></div>
  <div class="badge" style="left:762px"><i></i></div>
  <div class="badge" style="left:912px"><i></i></div>
</section>

<!-- FOOTER -->
<footer class="section footer">
  <div class="brand" style="left:161px;top:50px">
    <span class="brand-mark"></span>
    <span class="brand-name">Ridgeway Insulcoat Works</span>
  </div>
  <p class="about-text">Lorem ipsum dolor amet taxidermy poke knausgaard, next level adaptogen franzen leggings banh mi woke you probably haven't heard of them hell of vexillologist prism</p>
  <div class="follow">FOLLOW US <i></i><i></i><i></i><i></i></div>

  <h5 style="left:385px">Quick Links</h5>
  <div class="links">
    <span class="active">Home</span><span>Services</span><span>About</span>
    <span>Blog</span><span>FAQs</span><span>Why YS</span>
    <span>Contact</span><span>Work</span><span>About</span>
  </div>

  <h5 style="left:614px">Some News</h5>
  <p class="news" style="top:109px">Aenean tristique justo et nibh molestie, non porttitor eros suscipit</p>
  <p class="news" style="top:162px">Aenean tristique justo et nibh molestie, non porttitor eros suscipit</p>

  <h5 style="left:838px">Contact Us</h5>
  <div class="contact">
    <div><span class="label">Address</span><br>Unit 4, 118 Harlow Mill Road, Kestrel Falls 40213</div>
    <div><span class="label">E-mail</span><br>hello@ridgewayinsulcoat.example</div>
    <div><span class="label">Phone Number</span><br>+1 555 014 2297</div>
  </div>
</footer>
<div class="section copyright"><span><em>RidgewayInsulcoatWorks 2020</em> - All Rights Reserved</span></div>

</body>
</html>
```